MediKELP bottle concepts

Hello All,
We are developing a new ocean based supplement brand. The logo is attached to this project briefing.
What I am looking for is a look/feel/font selection to compliment this logo.
The family of products will be Migraine Prevention - Testosterone Booster + Antioxidants, Energy + Mental Clarity, Weight Management, Joint Pain Relief
Can you line up the bottles and make them look like a family.
Not a big fan of cartoon icons. This will be sold in an online pharmacy so I want the balance of looking clinical, but with an added freshness to denote these are ocean based supplements. Bottles will most likely be white.
Other things to add to the front of the bottle "30 Capsules - Dietary Supplement"
Don't worry about side panels or any details of that nature. It's just the front we are concerned with.
Have fun!

```html
<!DOCTYPE html>
<html lang="en">
<head>
<meta charset="utf-8">
<title>MediKELP Packaging Concept</title>
<link href="https://fonts.googleapis.com/css2?family=Montserrat:wght@400;700&family=Ubuntu:wght@300;400;500;700&display=swap" rel="stylesheet">
<style>
  :root {
    --sky: #93c8e6;
    --paper: #f6f6f6;
    --white: #ffffff;
    --ink-grey: #8a8a8a;
    --claim-box: #9aa5ac;
    --navy: #0d2f55;
    --plus-tint: #b9def3;
  }
  * { margin: 0; padding: 0; box-sizing: border-box; }
  html, body { width: 901px; height: 1200px; overflow: hidden; }
  body {
    position: relative;
    background: linear-gradient(var(--sky) 0 357px, var(--paper) 357px 100%);
    font-family: "Ubuntu", sans-serif;
  }
  .defs { position: absolute; width: 0; height: 0; }
  .concept-title {
    position: absolute; left: 46px; top: 40px;
    font-family: "Montserrat", sans-serif; font-weight: 400;
    font-size: 23px; color: var(--white); letter-spacing: 0.3px;
  }

  /* label: 1em = label width / 33; every position is a percentage of the label */
  .label {
    position: absolute;
    left: var(--x); top: var(--y);
    width: var(--w);
    aspect-ratio: 330 / 400;
    font-size: calc(var(--w) / 33);
    color: var(--white);
    --name-top: 44%;
    --name-size: 3.4em;
    --claim-top: 61%;
    --desc-top: 67.5%;
  }
  .label > * { position: absolute; white-space: nowrap; }
  .label-art { inset: 0; width: 100%; height: 100%; }
  .label-art .wave-light { fill: url(#waveLight); }
  .label-art .body { fill: url(#bodyBlue); }

  .brand {
    left: 62%; top: 15%; transform: translate(-50%, -50%);
    font-family: "Montserrat", sans-serif; font-weight: 700;
    font-size: 3em; line-height: 1;
  }
  .product-name {
    left: 9.5%; top: var(--name-top);
    font-size: var(--name-size);
    text-transform: uppercase; line-height: 0.9; letter-spacing: -0.01em;
  }
  .product-name .strong { font-weight: 500; display: block; }
  .product-name .light { font-weight: 300; display: block; }
  .product-name .plus { font-weight: 300; color: var(--plus-tint); }
  .claim {
    left: 9.5%; top: var(--claim-top);
    background: var(--claim-box); color: var(--navy);
    font-weight: 500; font-size: 1.3em; letter-spacing: 0.06em;
    padding: 0.05em 0.45em; line-height: 1.2;
  }
  .descriptor {
    left: 10%; top: var(--desc-top);
    font-size: 1.12em; line-height: 1.25; letter-spacing: 0.03em;
    font-weight: 400;
  }
  .count {
    left: 10%; top: 82.5%;
    font-weight: 300; font-size: 3.3em; line-height: 1;
  }
  .count small { font-size: 0.33em; font-weight: 500; letter-spacing: 0.04em; }
  .supplement {
    left: 11%; top: 92%;
    font-size: 1.05em; font-weight: 700; color: var(--navy); letter-spacing: 0.05em;
  }
  .seal {
    left: 76.4%; width: 15.5%; aspect-ratio: 1;
    border: 0.2em solid rgba(255,255,255,0.85); border-radius: 50%;
    transform: translateY(-50%);
  }
  .seal.one { top: 51%; }
  .seal.two { top: 67.5%; }
  .seal.three { top: 83.5%; }

  .label.energy  { --name-top: 46%; --name-size: 2.75em; --claim-top: 62%; --desc-top: 68%; }
  .label.booster { --name-top: 42%; --name-size: 2.6em;  --claim-top: 63%; --desc-top: 69.5%; }
  .label.migraine-bold { --name-top: 44%; --name-size: 3.2em; --claim-top: 62%; --desc-top: 68.5%; }
  .label.weight  { --name-top: 46%; --name-size: 2.85em; --claim-top: 62%; --desc-top: 68%; }

  .callout {
    position: absolute; font-family: "Montserrat", sans-serif;
    font-size: 16px; color: var(--ink-grey); letter-spacing: 1.2px; line-height: 1;
  }
  .callout.left { right: 684px; }
  .leader { position: absolute; height: 1px; background: var(--ink-grey); }
</style>
</head>
<body>
<svg class="defs" aria-hidden="true">
  <defs>
    <linearGradient id="waveLight" x1="0" y1="0" x2="1" y2="0">
      <stop offset="0" stop-color="#c2dcec"/><stop offset="1" stop-color="#7fbde4"/>
    </linearGradient>
    <linearGradient id="bodyBlue" x1="0" y1="0" x2="0.3" y2="1">
      <stop offset="0" stop-color="#1374bd"/><stop offset="1" stop-color="#6cc4ee"/>
    </linearGradient>
    <linearGradient id="bandOrange" x1="0" x2="1"><stop offset="0" stop-color="#d9a07e"/><stop offset="0.2" stop-color="#f1d9c2"/><stop offset="0.5" stop-color="#e8843a"/><stop offset="1" stop-color="#e67b2e"/></linearGradient>
    <linearGradient id="bandSilver" x1="0" x2="1"><stop offset="0" stop-color="#b3b5b8"/><stop offset="0.25" stop-color="#e3e4e5"/><stop offset="0.55" stop-color="#97999c"/><stop offset="1" stop-color="#8a8c8f"/></linearGradient>
    <linearGradient id="bandGreen" x1="0" x2="1"><stop offset="0" stop-color="#a8d08d"/><stop offset="0.2" stop-color="#d6e9c3"/><stop offset="0.5" stop-color="#6bb344"/><stop offset="1" stop-color="#5fa83a"/></linearGradient>
    <linearGradient id="bandGold" x1="0" x2="1"><stop offset="0" stop-color="#d7c07d"/><stop offset="0.2" stop-color="#efe3bd"/><stop offset="0.5" stop-color="#c9a43c"/><stop offset="1" stop-color="#bf9934"/></linearGradient>
    <linearGradient id="bandPurple" x1="0" x2="1"><stop offset="0" stop-color="#b79fc9"/><stop offset="0.2" stop-color="#e5dced"/><stop offset="0.5" stop-color="#7e4f9f"/><stop offset="1" stop-color="#733f95"/></linearGradient>
    <clipPath id="labelClip" clipPathUnits="userSpaceOnUse"><rect x="0" y="0" width="330" height="400" rx="16"/></clipPath>
  </defs>
</svg>

<h1 class="concept-title">MediKELP Packaging Concept</h1>

<article class="label energy" style="--x:43px; --y:239px; --w:144px">
  <svg class="label-art" viewBox="0 0 330 400" preserveAspectRatio="none" aria-hidden="true"><g clip-path="url(#labelClip)">
    <rect class="wave-light" width="330" height="400"/>
    <path class="body" d="M0,150 C60,125 120,115 185,130 C245,145 290,130 330,108 V400 H0 Z"/>
    <path fill="url(#bandOrange)" d="M0,0 H330 V82 C300,118 240,132 170,124 C110,116 60,76 0,86 Z"/>
  </g></svg>
  <span class="brand">MediKELP</span>
  <h2 class="product-name"><span class="strong">Energy<span class="plus">+</span></span><span class="light">Mental Clarity</span></h2>
  <p class="claim">OCEAN BASED FORMULA</p>
  <p class="descriptor">Promotes healthy brain<br>function and migraine related<br>symtoms relief</p>
  <p class="count">30 <small>CAPSULES</small></p>
  <p class="supplement">DIETARY SUPPLEMENT</p>
  <span class="seal one"></span><span class="seal two"></span><span class="seal three"></span>
</article>

<article class="label booster" style="--x:197px; --y:241px; --w:155px">
  <svg class="label-art" viewBox="0 0 330 400" preserveAspectRatio="none" aria-hidden="true"><g clip-path="url(#labelClip)">
    <rect class="wave-light" width="330" height="400"/>
    <path class="body" d="M0,150 C60,125 120,115 185,130 C245,145 290,130 330,108 V400 H0 Z"/>
    <path fill="url(#bandSilver)" d="M0,0 H330 V82 C300,118 240,132 170,124 C110,116 60,76 0,86 Z"/>
  </g></svg>
  <span class="brand">MediKELP</span>
  <h2 class="product-name"><span class="strong">Testosterone</span><span class="strong">Booster<span class="plus">+</span></span><span class="light">Antoxidants</span></h2>
  <p class="claim">OCEAN BASED FORMULA</p>
  <p class="descriptor">Promotes healthy brain<br>function and migraine related<br>symtoms relief</p>
  <p class="count">30 <small>CAPSULES</small></p>
  <p class="supplement">DIETARY SUPPLEMENT</p>
  <span class="seal one"></span><span class="seal two"></span><span class="seal three"></span>
</article>

<article class="label" style="--x:362px; --y:234px; --w:179px">
  <svg class="label-art" viewBox="0 0 330 400" preserveAspectRatio="none" aria-hidden="true"><g clip-path="url(#labelClip)">
    <rect class="wave-light" width="330" height="400"/>
    <path class="body" d="M0,150 C60,125 120,115 185,130 C245,145 290,130 330,108 V400 H0 Z"/>
    <path fill="url(#bandGreen)" d="M0,0 H330 V82 C300,118 240,132 170,124 C110,116 60,76 0,86 Z"/>
  </g></svg>
  <span class="brand">MediKELP</span>
  <h2 class="product-name"><span class="strong">Migraine</span><span class="light">Prevention</span></h2>
  <p class="claim">OCEAN BASED FORMULA</p>
  <p class="descriptor">Promotes healthy brain<br>function and migraine related<br>symtoms relief</p>
  <p class="count">30 <small>CAPSULES</small></p>
  <p class="supplement">DIETARY SUPPLEMENT</p>
  <span class="seal one"></span><span class="seal two"></span><span class="seal three"></span>
</article>

<article class="label migraine-bold" style="--x:551px; --y:243px; --w:154px">
  <svg class="label-art" viewBox="0 0 330 400" preserveAspectRatio="none" aria-hidden="true"><g clip-path="url(#labelClip)">
    <rect class="wave-light" width="330" height="400"/>
    <path class="body" d="M0,150 C60,125 120,115 185,130 C245,145 290,130 330,108 V400 H0 Z"/>
    <path fill="url(#bandGold)" d="M0,0 H330 V82 C300,118 240,132 170,124 C110,116 60,76 0,86 Z"/>
  </g></svg>
  <span class="brand">MediKELP</span>
  <h2 class="product-name"><span class="strong">Migraine</span><span class="strong">Prevention</span></h2>
  <p class="claim">OCEAN BASED FORMULA</p>
  <p class="descriptor">Promotes healthy brain<br>function and migraine related<br>symtoms relief</p>
  <p class="count">30 <small>CAPSULES</small></p>
  <p class="supplement">DIETARY SUPPLEMENT</p>
  <span class="seal one"></span><span class="seal two"></span><span class="seal three"></span>
</article>

<article class="label weight" style="--x:713px; --y:244px; --w:146px">
  <svg class="label-art" viewBox="0 0 330 400" preserveAspectRatio="none" aria-hidden="true"><g clip-path="url(#labelClip)">
    <rect class="wave-light" width="330" height="400"/>
    <path class="body" d="M0,150 C60,125 120,115 185,130 C245,145 290,130 330,108 V400 H0 Z"/>
    <path fill="url(#bandPurple)" d="M0,0 H330 V82 C300,118 240,132 170,124 C110,116 60,76 0,86 Z"/>
  </g></svg>
  <span class="brand">MediKELP</span>
  <h2 class="product-name"><span class="strong">Weight</span><span class="strong">Management</span></h2>
  <p class="claim">OCEAN BASED FORMULA</p>
  <p class="descriptor">Promotes healthy brain<br>function and migraine related<br>symtoms relief</p>
  <p class="count">30 <small>CAPSULES</small></p>
  <p class="supplement">DIETARY SUPPLEMENT</p>
  <span class="seal one"></span><span class="seal two"></span><span class="seal three"></span>
</article>

<article class="label hero" style="--x:303px; --y:723px; --w:290px">
  <svg class="label-art" viewBox="0 0 330 400" preserveAspectRatio="none" aria-hidden="true"><g clip-path="url(#labelClip)">
    <rect class="wave-light" width="330" height="400"/>
    <path class="body" d="M0,150 C60,125 120,115 185,130 C245,145 290,130 330,108 V400 H0 Z"/>
    <path fill="url(#bandGreen)" d="M0,0 H330 V82 C300,118 240,132 170,124 C110,116 60,76 0,86 Z"/>
  </g></svg>
  <span class="brand">MediKELP</span>
  <h2 class="product-name"><span class="strong">Migraine</span><span class="light">Prevention</span></h2>
  <p class="claim">OCEAN BASED FORMULA</p>
  <p class="descriptor">Promotes healthy brain<br>function and migraine related<br>symtoms relief</p>
  <p class="count">30 <small>CAPSULES</small></p>
  <p class="supplement">DIETARY SUPPLEMENT</p>
  <span class="seal one"></span><span class="seal two"></span><span class="seal three"></span>
</article>

<span class="leader" style="left:597px; top:771px; width:73px"></span>
<span class="callout" style="left:678px; top:763px">BRAND LOGO</span>

<span class="callout left" style="top:814px">WAVE</span>
<span class="leader" style="left:222px; top:822px; width:95px"></span>

<span class="callout left" style="top:899px">PRODUCT NAME</span>
<span class="leader" style="left:222px; top:907px; width:108px"></span>

<span class="callout left" style="top:933px">CLAIM</span>
<span class="leader" style="left:222px; top:941px; width:95px"></span>

<span class="callout left" style="top:970px">DESCRIPTOR</span>
<span class="leader" style="left:222px; top:978px; width:95px"></span>
</body>
</html>
```